Flyer/Poster design required for volunteer activities

We need a STRIKING A4 Poster/Flyer advertising our conservation volunteer program activities which are currently happening in the area. This poster is to advertise the program once people have arrived on the island or to locals. The program covers 5 months, May-September 2019 and is focused on conservation. I have attached the following:
- a flyer which was previously created (QMR Habitat Helpers 2019 sm)to advertise the program - would prefer it has a similar striking resemblance, but not essential
- A mock up document 'HHQMR On Island Poster_2019_v2' with text -Logos-Images

Target Market(s)

Everyone interested in Environmental Adventure/Hiking/Citizen Science

Industry/Entity Type

Tourism

Font styles to use
Sans Serif

Requirements
Must have
• -A travel conservation focus
• -Must use 'QMR-Background Image' as the background to the design
• -The info of where to get more information and the social media details must be prominent

```html
<!DOCTYPE html>
<html lang="en">
<head>
<meta charset="utf-8">
<title>QMR Habitat Helpers – Program 2019</title>
<link rel="stylesheet" href="https://fonts.googleapis.com/css2?family=Mulish:wght@800;900&family=Open+Sans:wght@600;700;800&family=Libre+Baskerville&display=swap">
<style>
:root{
  --blue:#0a6fc2;
  --navy:#0d2a55;
  --yellow:#ffe01b;
  --gold:#fcd45a;
  --white:#ffffff;
  --band:rgba(18,28,42,.88);
  --sea-top:#c9dfee;
  --sea-mid:#3f86ab;
  --land:#3d5a3a;
  --deep:#1e3a3e;
}
*{margin:0;padding:0;box-sizing:border-box}
html,body{width:850px;height:1200px;overflow:hidden;background:#fff}
.poster{position:relative;width:850px;height:1200px;overflow:hidden;font-family:"Open Sans",sans-serif;color:var(--white)}
.backdrop{position:absolute;inset:0;background:
  linear-gradient(180deg,var(--sea-top) 0%,#e6eef4 14%,#7fb2cc 22%,var(--sea-mid) 34%,#3f7f86 48%,var(--land) 62%,#2d4632 78%,var(--deep) 100%)}
.frame{position:absolute;left:18px;top:18px;width:814px;height:1164px;border:4px solid var(--yellow)}
.title{position:absolute;left:50px;top:52px;width:610px;text-align:center;font-family:"Mulish",sans-serif;font-weight:900;color:var(--blue);font-size:45px;line-height:55px;letter-spacing:.5px}
.brand{position:absolute;left:660px;top:70px;width:150px;display:flex;flex-direction:column;align-items:center;gap:6px}
.brand-dot{width:70px;height:70px;border-radius:50%;background:var(--blue)}
.brand-name{font-family:"Mulish",sans-serif;font-weight:900;color:var(--blue);font-size:17px;text-align:center;line-height:20px}
.season{position:absolute;left:236px;top:179px;width:389px;height:50px;background:var(--gold);color:var(--blue);font-family:"Mulish",sans-serif;font-weight:900;font-size:36px;text-align:center;line-height:52px}
.invite{position:absolute;left:0;top:238px;width:850px;height:77px;background:var(--band);text-align:center;color:var(--yellow);font-weight:800;font-size:26px;line-height:29px;padding-top:12px;letter-spacing:-.2px}
.month{position:absolute;left:37px;width:763px;border:3px solid var(--yellow)}
.month-tag{position:absolute;left:229px;top:-3px;width:290px;height:38px;background:var(--gold);text-align:center}
.month-tag h2{font-family:"Open Sans",sans-serif;font-weight:800;color:var(--blue);font-size:16px;line-height:17px;padding-top:2px}
.month-tag p{font-family:"Libre Baskerville",serif;color:var(--blue);font-size:13px;line-height:17px}
.month-tag p.light{color:var(--white)}
.month-tag sup{font-size:8px}
.theme{display:inline-block;background:rgba(20,30,40,.75);font-weight:700;font-size:11px;line-height:15px;padding:0 35px 0 6px;margin-bottom:3px}
.acts{list-style:none;font-weight:700;font-size:11px;line-height:17px;text-shadow:0 1px 2px rgba(0,0,0,.6);white-space:nowrap}
.right{text-align:right}
.big .acts{font-size:13.3px;line-height:17px}
.big .theme{background:none;font-size:13.3px;line-height:17px;padding:0;margin-bottom:0}
.photo{position:absolute;border:1px solid rgba(255,255,255,.5)}
.footer{position:absolute;left:0;top:1133px;width:850px;text-align:center;font-weight:800;font-size:13.5px;line-height:18px}
.footer .gap{display:inline-block;width:26px}
</style>
</head>
<body>
<div class="poster">
  <div class="backdrop" role="img" aria-label="Aerial view of the island coastline, lagoon and forested ridges"></div>
  <div class="frame"></div>

  <h1 class="title">QUOLL MARSH RIDGE HABITAT HELPERS</h1>
  <div class="brand"><span class="brand-dot"></span><span class="brand-name">QMR Habitat Helpers</span></div>
  <div class="season">MAY - SEPTEMBER</div>

  <div class="invite">BE INVOLED IN PRESERVING PARADISE<br>JOIN THE QMR HABITAT HELPERS PROGRAM 2019</div>

  <section class="month" style="top:323px;height:172px">
    <div class="month-tag"><h2>MAY 2019</h2><p class="light">Feature Week: 19<sup>th</sup> – 26<sup>th</sup> May</p></div>
    <div style="position:absolute;left:6px;top:56px">
      <span class="theme">BIRDS OF QUOLL MARSH RIDGE</span>
      <ul class="acts" style="line-height:18px">
        <li>-Ocean bird watching boat trips</li>
        <li>-Guided tours of Woodhen and Currawong quarters</li>
        <li>-Weekly lectures at the Quoll Marsh Ridge Museum</li>
        <li>-Weekly screenings of documentaries on Bird and Island Conservation projects</li>
        <li>-Self guided land bird survey tours</li>
      </ul>
    </div>
    <div class="photo" role="img" aria-label="Grey seabird resting among green leaves" style="left:600px;top:20px;width:138px;height:133px;background:linear-gradient(135deg,#5d6a4a,#8a8f86 50%,#3b4a30)"></div>
  </section>

  <section class="month" style="top:502px;height:174px">
    <div class="month-tag"><h2>JUNE 2019</h2><p>Feature Week: 3<sup>th</sup> – 9<sup>th</sup> June</p></div>
    <div class="photo" role="img" aria-label="Snorkeller recording a marine survey underwater" style="left:15px;top:55px;width:151px;height:107px;background:linear-gradient(180deg,#4da7d8,#1f6ea4 60%,#1b4f7a)"></div>
    <div class="right" style="position:absolute;right:8px;top:48px">
      <span class="theme" style="background:none;padding:0">QUOLL MARSH RIDGE MARINE PARK</span>
      <ul class="acts" style="line-height:20.5px">
        <li>-Marine pest monitoring with marine park staff</li>
        <li>-Marine plastic &amp; debris clean up activities</li>
        <li>-Screenings of marine conservation documentaries at the museum</li>
        <li>-Weekly lectures on Marine Life at the Quoll Marsh Ridge Museum</li>
        <li>-Marine Activities with local operators</li>
      </ul>
    </div>
  </section>

  <section class="month" style="top:685px;height:137px">
    <div class="month-tag"><h2>JULY 2019</h2><p>Feature Week: 21<sup>st</sup> – 28<sup>th</sup> July</p></div>
    <div style="position:absolute;left:6px;top:22px">
      <span class="theme" style="padding-right:70px">INVASIVE SPECIES</span>
      <ul class="acts" style="line-height:18px">
        <li>-Guided walks to learn about the weed eradication program</li>
        <li>-Weekly lectures on plants of Quoll Marsh Ridge</li>
        <li>-Weekly screenings of documentaries on plant and island conservation projects</li>
        <li>-Guided walks to Mount Garrow</li>
        <li>-Local tour guides include commentaries on island plants</li>
      </ul>
    </div>
    <div class="photo" role="img" aria-label="Hiker on a forest track among palm trees" style="left:624px;top:10px;width:114px;height:114px;background:linear-gradient(160deg,#4c6b34,#2a3d22 60%,#6d7a56)"></div>
  </section>

  <section class="month big" style="top:831px;height:128px">
    <div class="month-tag"><h2>AUGUST 2019</h2><p>Feature Week: 11<sup>th</sup> – 19<sup>th</sup> August</p></div>
    <div class="photo" role="img" aria-label="Hands holding a large dark stick insect" style="left:15px;top:14px;width:141px;height:104px;background:linear-gradient(135deg,#d9c7b8,#b99a84 50%,#3a3430)"></div>
    <div class="right" style="position:absolute;right:8px;top:33px">
      <span class="theme">AMAZING INVERTEBRATES</span>
      <ul class="acts">
        <li>-Guided night walks to learn about the island's invertebrates</li>
        <li>-Weekly viewing and presentation of the Quoll Marsh Ridge Phasmid</li>
        <li>-Weekly lectures on invertebrates of Quoll Marsh Ridge at the museum</li>
        <li>-Weekly screenings of documentaries on island conservation projects</li>
      </ul>
    </div>
  </section>

  <section class="month big" style="top:973px;height:146px">
    <div class="month-tag"><h2>SEPTEMBER 2019</h2><p>Feature Week: 1<sup>st</sup> – 8<sup>th</sup> September</p></div>
    <div style="position:absolute;left:10px;top:36px;width:620px">
      <span class="theme">PROTECTING PARADISE</span>
      <ul class="acts">
        <li>-Observational snorkel surveys with Marine Ecologists, to assess populations of Ridgeline<br>Anemonefish and other unique fish species</li>
        <li>-Guided snorkel and glass bottom boat tour to assess coral health within the<br>Quoll Marsh Ridge Marine Park</li>
        <li>-Guided walks to learn about the island's conservation history</li>
      </ul>
    </div>
    <div class="photo" role="img" aria-label="Map of the island and its marine park" style="left:633px;top:25px;width:119px;height:89px;background:linear-gradient(135deg,#8fd0d8,#5bb3bf 55%,#4a9a5a)"></div>
  </section>

  <div class="footer">See the QMR visitor centre for more information about the QMR Habitat Helpers program for 2019<br>FOLLOW US!<span class="gap"></span>www.hhqmr.org/news&nbsp;&nbsp;photos@hhqmr</div>
</div>
</body>
</html>
```